Photo Booth and Chocolate Fountain Rental Flyer

I need a design that looks appealing and elegant for people who are having parties or weddings. It is a photo booth and chocolate fountain rental company. I would like it to look fun for the photo booth and delicious for the chocolate fountain. I would like some pictures to showcase the services and pricing options on it too. My logo needs to be put somewhere on the flyer also. You can check out my website for more information www.tvr-parties.com I want it to be a little different from the website and contain pictures of photo booth strips and chocolate fountains.

Industry/Entity Type

It Company

Requirements
Must have
• Must Have:
- our logo
our contact info
imagery of the photobooth experience
editable (change specials and marketing)
works in color
Nice to have
• A backside with the different packages of the photo booth and fountain

```html
<!DOCTYPE html>
<html lang="en">
<head>
<meta charset="utf-8">
<title>Dulcea Events – Flyer</title>
<link href="https://fonts.googleapis.com/css2?family=Poppins:wght@300;400;600&display=swap" rel="stylesheet">
<style>
  :root {
    --chocolate-dark: #3f2310;
    --chocolate: #6a3d1c;
    --chocolate-light: #8e5a30;
    --panel: #e9e5e7;
    --panel-sheen: #f7f5f6;
    --panel-shade: #d6d0d3;
    --gold-edge: #d8c24a;
    --olive: #75651a;
    --olive-strong: #6a5a0e;
    --logo-gold: #9b7a2a;
  }
  * { margin: 0; padding: 0; box-sizing: border-box; }
  html, body { width: 848px; height: 1200px; overflow: hidden; }
  body {
    position: relative;
    font-family: "Poppins", "Century Gothic", sans-serif;
    color: var(--olive);
    background:
      linear-gradient(160deg, rgba(255,255,255,0.10) 0%, transparent 30%, rgba(255,255,255,0.08) 55%, transparent 75%),
      radial-gradient(ellipse at 60% 45%, var(--chocolate-light) 0%, var(--chocolate) 45%, var(--chocolate-dark) 100%);
  }
  .panel {
    position: absolute;
    border-radius: 30px;
    border: 2px solid var(--gold-edge);
    box-shadow: 0 0 8px rgba(230, 210, 90, 0.8);
    background:
      linear-gradient(115deg, transparent 0%, rgba(255,255,255,0.55) 18%, transparent 30%, rgba(255,255,255,0.45) 48%, transparent 62%, rgba(255,255,255,0.5) 80%, transparent 95%),
      linear-gradient(180deg, var(--panel-sheen), var(--panel) 50%, var(--panel-shade));
  }
  .panel--gallery { left: 22px; top: 40px; width: 384px; height: 1120px; }
  .panel--intro { left: 441px; top: 45px; width: 385px; height: 465px; }
  .panel--contact { left: 441px; top: 545px; width: 385px; height: 612px; }

  .brand {
    position: absolute; left: 40px; top: 80px; width: 346px; height: 170px;
    display: flex; align-items: center; justify-content: center;
    font-weight: 400; font-size: 46px; white-space: nowrap;
    color: var(--logo-gold);
  }

  .photo {
    position: absolute; left: 40px; width: 346px;
    box-shadow: inset 0 0 30px rgba(255,255,255,0.35);
  }
  .photo--fountain { top: 276px; height: 268px;
    background: radial-gradient(ellipse at 35% 40%, #a0623a 0%, #6e3a22 45%, #4d2a2e 100%); }
  .photo--couple { top: 559px; height: 269px;
    background: linear-gradient(180deg, #b7ada4 0%, #a39a90 55%, #c2b6a6 100%); }
  .photo--party { top: 843px; height: 268px;
    background: linear-gradient(180deg, #b9c4cc 0%, #d6c3c4 45%, #e2b8c8 100%); }

  .copy { position: absolute; right: 18px; text-align: right; white-space: nowrap; }
  .headline { font-weight: 300; }
  .headline strong { font-weight: 600; color: var(--olive-strong); }
  .body-text { font-size: 18px; line-height: 25.5px; font-weight: 300; }

  .intro-headline { top: 18px; font-size: 32px; line-height: 48px; }
  .intro-headline strong { font-size: 36px; }
  .intro-quote { top: 239px; }

  .wait-headline { top: 26px; font-size: 33px; line-height: 42px; }
  .wait-body { top: 134px; }
  .prices-headline { top: 297px; font-size: 33px; line-height: 48px; }
  .prices-headline strong { font-size: 37px; }
  .contact-lines { top: 536px; }
</style>
</head>
<body>

  <section class="panel panel--gallery"></section>
  <div class="brand">Dulcea Events</div>
  <div class="photo photo--fountain" role="img" aria-label="Chocolate fountain with melted chocolate cascading over tiers, draped fabric behind"></div>
  <div class="photo photo--couple" role="img" aria-label="Newlywed couple running hand in hand on a beach"></div>
  <div class="photo photo--party" role="img" aria-label="Mother and two girls celebrating a birthday with balloons and gifts"></div>

  <section class="panel panel--intro">
    <h1 class="copy headline intro-headline">
      Make your events<br>
      <strong>appealing</strong> &amp;<br>
      <strong>unforgettable</strong><br>
      with our specialties.
    </h1>
    <p class="copy body-text intro-quote">“We are a one of a kind event<br>company, specializing in offering<br>you fabulous fun in our photo<br>booth, delicious chocolate<br>fountains, and one of a kind<br>decor. We can proudly say that<br>our company successfully makes<br>people’s dreams a reality.”</p>
  </section>

  <section class="panel panel--contact">
    <h2 class="copy headline wait-headline">What are <strong>you</strong><br>waiting for?</h2>
    <p class="copy body-text wait-body">Let us make your event enticing<br>with lots of amazing decor,<br>delicious chocolate and<br>excellent photos!</p>
    <p class="copy headline prices-headline"><strong>Please</strong> feel free<br>to <strong>contact us</strong><br>for our full range<br>of <strong>prices</strong></p>
    <p class="copy body-text contact-lines">Call: 555-014-2287<br>Web: www.tvr-parties.com</p>
  </section>

</body>
</html>
```